Harrowgate Distillery Bottle Label Design

We need a label design for a product called "Cedar Lorne Straight Bourbon Whiskey". The bottle has two embossments on the side and an image printed on the back that will show through when looking from the front (shown in the attached image). It's made of 30% rye and 70% corn; images of the ingredients can be incorporated into the label design. We are a distillery that produces whiskey and bourbon from local farmers around the area. We focus on the quality of the ingredients and using the recipes passed down from generation to generation. We like a straight forward design using two colors maximum. The background will be brown once filled with the bourbon, so it must contrast against it (i.e. white and other lighter colors). The Harrowgate Distillery logo must be present on the bottle front, as well as 750 ml, 84 PROOF, 42% ALC/VOL.

Target Market(s)

Craft whiskey consumers.

Industry/Entity Type

Product

Colors
fee18a
fbe7d2
fff3d1
fefcee
fefdec
fdf9cf

Requirements
Must have
• 750 ml, 84 PROOF, 42% ALC/VOL. Aged for 3 years.The Harrowgate Distillery logo must be present on the bottle. Only two colors on label.
Nice to have
• Story of how we are a micro distillery making hand crafted whiskey.
Should not have
• False or misleading print.

```html
<!DOCTYPE html>
<html lang="en">
<head>
<meta charset="utf-8">
<title>Harrowgate Distillery – Cedar Lorne Straight Bourbon Whiskey Label</title>
<link rel="stylesheet" href="https://fonts.googleapis.com/css2?family=Oswald:wght@400;500;600&family=Playfair+Display:ital@1&display=swap">
<style>
  :root {
    --page: #ececec;
    --bourbon-light: #d98424;
    --bourbon-mid: #b25a16;
    --bourbon-deep: #7e3510;
    --gold: #fee18a;
    --cream: #fff3d1;
    --ink: #8a3a0e;
  }
  * { box-sizing: border-box; margin: 0; padding: 0; }
  html, body { width: 1200px; height: 1000px; overflow: hidden; }
  body { background: var(--page); position: relative; font-family: "Oswald", sans-serif; }

  .label {
    position: absolute; left: 320px; top: 30px; width: 560px; height: 940px;
    background: linear-gradient(180deg, var(--bourbon-light) 0%, var(--bourbon-mid) 55%, var(--bourbon-deep) 100%);
    border-radius: 8px; overflow: hidden;
    display: flex; flex-direction: column; align-items: center;
    color: var(--gold);
  }

  .farm-photo {
    position: absolute; left: 0; right: 0; top: 580px; bottom: 0;
    background: linear-gradient(180deg, rgba(120,55,20,0) 0%, rgba(115,55,22,0.45) 40%, rgba(110,55,22,0.55) 100%);
  }

  .brand { position: relative; margin-top: 40px; display: flex; flex-direction: column; align-items: center; }
  .brand-dot { width: 56px; height: 56px; border-radius: 50%; background: var(--gold); margin-bottom: 14px; }
  .brand-name { font-weight: 600; color: var(--gold); text-align: center; line-height: 1; }
  .brand-name .big { display: block; font-size: 54px; letter-spacing: 1px; }
  .brand-name .small { display: block; font-size: 20px; letter-spacing: 8px; margin-top: 6px;
    border-top: 2px solid var(--gold); border-bottom: 2px solid var(--gold); padding: 2px 0; }

  .flourish { position: relative; width: 230px; height: 22px; background: rgba(254,225,138,0.35); border-radius: 11px; flex: none; }
  .flourish.top { margin-top: 24px; }
  .flourish.bottom { margin-top: 12px; }

  .product { position: relative; text-align: center; line-height: 1; margin-top: 10px; }
  .product .origin { display: block; font-size: 46px; font-weight: 500; letter-spacing: 4px; color: var(--gold); }
  .product .style { display: inline-block; font-size: 40px; font-weight: 500; letter-spacing: 4px;
    background: var(--gold); color: var(--ink); padding: 2px 14px; margin-top: 6px; }
  .product .spirit { display: block; font-size: 80px; font-weight: 500; color: var(--cream); margin-top: 6px; letter-spacing: 1px; }

  .age-ribbon { position: relative; margin-top: 16px; width: 300px; height: 54px; flex: none; }
  .age-ribbon svg { position: absolute; inset: 0; }
  .age-ribbon span { position: absolute; inset: 0 0 8px 0; display: flex; align-items: center; justify-content: center;
    font-size: 22px; font-weight: 500; color: var(--ink); letter-spacing: 1px; }

  .story { position: relative; width: 460px; margin-top: 14px; text-align: center;
    font-family: "Playfair Display", serif; font-style: italic; font-size: 15px; line-height: 1.6; color: var(--gold); }

  .grain { position: relative; width: 160px; height: 48px; margin-top: 10px; flex: none;
    background: rgba(254,225,138,0.3); border-radius: 50% 50% 10px 10px; }

  .spec-bar { position: relative; margin-top: auto; margin-bottom: 40px; width: 480px; display: flex;
    border: 2px solid var(--gold); flex: none; }
  .spec-bar span { flex: 1; text-align: center; font-size: 26px; font-weight: 500; padding: 4px 0; color: var(--gold); }
  .spec-bar span + span { border-left: 2px solid var(--gold); }
</style>
</head>
<body>
  <main class="label">
    <div class="farm-photo" role="img" aria-label="Photograph of a red barn and grain silos on a farm"></div>

    <header class="brand">
      <div class="brand-dot"></div>
      <h1 class="brand-name"><span class="big">Harrowgate</span><span class="small">DISTILLERY</span></h1>
    </header>

    <div class="flourish top" role="img" aria-label="Decorative scroll flourish"></div>

    <h2 class="product">
      <span class="origin">CEDAR LORNE</span>
      <span class="style">STRAIGHT</span>
      <span class="spirit">BOURBON<br>WHISKEY</span>
    </h2>

    <div class="flourish bottom" role="img" aria-label="Decorative scroll flourish"></div>

    <div class="age-ribbon">
      <svg viewBox="0 0 300 54" width="300" height="54">
        <polygon points="0,14 36,14 36,50 0,50 12,32" fill="#fee18a"/>
        <polygon points="300,14 264,14 264,50 300,50 288,32" fill="#fee18a"/>
        <rect x="24" y="4" width="252" height="42" fill="#fee18a" stroke="#8a3a0e" stroke-width="2"/>
        <rect x="30" y="9" width="240" height="32" fill="none" stroke="#8a3a0e" stroke-width="1.5"/>
      </svg>
      <span>AGED FOR 3 YEARS</span>
    </div>

    <p class="story">This handcrafted bourbon comes from our distillery based in the heart of the pristine lake county of Brannock, Wendell Valley. All our ingredients are carefully hand selected and grown local, everything we need to make great tasting whiskey.</p>

    <div class="grain" role="img" aria-label="Crossed wheat stalks illustration"></div>

    <div class="spec-bar">
      <span>84 PROOF</span>
      <span>42%ALC/VOL</span>
      <span>750ml</span>
    </div>
  </main>
</body>
</html>
```